Bluewater Products Flyer

Bluewater Lending Group, Inc.
Licensed Mortgage Company
Serving the DMV since 1997
"You choose Bluewater, we'll carry it home"
We specialize in...
FHA Loans
* Credit Scores as low as 500
* 203K Renovation Loans
Conventional Loans
* As little as 1% Down
* Bank Statement for Self-Employed
Investor Loans
* DSCR, & Fix & Flip
* Commercial & New Construction
Other Programs
* HELOCS & Reverse Mortgages
Call today for a free consultation
(800) 641-2957
www.bluewaterlendhub.com
NMLS #731846

```html
<!DOCTYPE html>
<html lang="en">
<head>
<meta charset="utf-8">
<title>Bluewater Lending Group – Products Flyer</title>
<link href="https://fonts.googleapis.com/css2?family=Cinzel:wght@500;700&family=Libre+Caslon+Text:ital,wght@0,400;1,700&family=Outfit:wght@400;500;600;700&display=swap" rel="stylesheet">
<style>
  :root{
    --backdrop:#979797;
    --paper:#ffffff;
    --navy:#1f4c9c;
    --deep-blue:#0f5b8c;
    --gold:#d9a24a;
    --lime:#a6cf38;
    --olive:#bda93a;
    --ink:#151515;
    --charcoal:#4a4a4c;
    --photo-top:#bdb7a5;
    --photo-mid:#6e8a4a;
    --photo-low:#4d8a2c;
  }
  *{box-sizing:border-box;margin:0;padding:0}
  html,body{width:1058px;height:1200px;overflow:hidden;background:var(--backdrop)}
  .canvas{position:relative;width:1058px;height:1200px;background:var(--backdrop)}
  .flyer{position:absolute;left:129px;top:92px;width:787px;height:1018px;background:var(--paper);overflow:hidden}
  .hero-photo{position:absolute;left:0;top:0;width:787px;height:463px;
    background:linear-gradient(180deg,var(--photo-top) 0%,#a9a592 35%,var(--photo-mid) 65%,var(--photo-low) 100%)}
  .hero-arch{position:absolute;left:0;top:0;width:787px;height:463px}
  .headline{position:absolute;left:0;width:787px;text-align:center}
  .headline-lead{top:330px;font-family:'Cinzel',serif;font-weight:500;font-size:31px;color:var(--gold);letter-spacing:1px}
  .headline-main{top:360px;font-family:'Cinzel',serif;font-weight:700;font-size:60px;color:var(--navy);letter-spacing:1px}
  .headline-tag{top:432px;display:flex;justify-content:center;align-items:flex-end;gap:4px}
  .headline-tag span{font-family:'Libre Caslon Text',serif;font-style:italic;font-weight:700;font-size:28px;color:var(--ink);line-height:1}
  .headline-tag i{display:block;width:74px;height:1.5px;background:var(--ink);margin-bottom:2px}
  .section-title{position:absolute;top:518px;left:0;width:787px;display:flex;justify-content:center;align-items:center;gap:10px}
  .section-title h2{font-family:'Libre Caslon Text',serif;font-weight:400;font-size:35px;color:var(--ink)}
  .section-title i{display:block;width:62px;height:2px;background:var(--gold)}
  .product-card{position:absolute;top:621px;width:218px;height:197px;border:1.5px solid var(--deep-blue);border-radius:12px;padding:44px 14px 0 27px}
  .card-fha{left:56px}.card-conv{left:292px}.card-inv{left:528px}
  .card-icon{position:absolute;top:-52px;left:26px;width:86px;height:86px;border-radius:50%;display:flex;align-items:center;justify-content:center}
  .card-fha .card-icon{background:var(--deep-blue)}
  .card-conv .card-icon{background:var(--lime)}
  .card-inv .card-icon{background:var(--olive)}
  .product-card h3{font-family:'Outfit',sans-serif;font-weight:600;font-size:24px;line-height:30px;color:var(--ink);margin-bottom:10px}
  .product-card ul{list-style:none}
  .product-card li{position:relative;font-family:'Outfit',sans-serif;font-size:17px;line-height:21px;color:var(--ink);padding-left:23px;margin-bottom:4px}
  .product-card li svg{position:absolute;left:0;top:3px}
  .other-programs{position:absolute;top:838px;left:298px;z-index:3;font-family:'Outfit',sans-serif;font-size:19px;line-height:24px;color:var(--ink);display:flex;align-items:center;white-space:nowrap}
  .other-programs strong{font-weight:600}
  .other-programs i{display:block;width:1.5px;height:24px;background:var(--gold);margin:0 12px}
  .brand-seal{position:absolute;left:-6px;top:850px;width:246px;height:246px;border-radius:50%;border:2px solid var(--charcoal);background:var(--paper);display:flex;align-items:flex-start;justify-content:center;padding-top:88px;gap:8px;z-index:2}
  .brand-seal .brand-dot{width:14px;height:14px;border-radius:50%;background:var(--navy);margin-top:9px}
  .brand-seal .brand-name{font-family:'Outfit',sans-serif;font-weight:700;font-size:28px;color:var(--navy)}
  .cta-band{position:absolute;left:244px;top:926px;width:543px;height:43px;background:var(--lime);display:flex;align-items:center;padding-left:23px;gap:8px}
  .cta-band .cta-text{font-family:'Outfit',sans-serif;font-weight:600;font-size:20px;color:var(--ink)}
  .cta-band .cta-phone{font-family:'Outfit',sans-serif;font-weight:600;font-size:20px;color:var(--deep-blue);display:flex;align-items:center;gap:4px}
  .contact-band{position:absolute;left:240px;top:969px;width:547px;height:49px;background:var(--charcoal);display:flex;align-items:center;padding-left:27px;font-family:'Outfit',sans-serif;font-size:19px;color:#fff}
  .contact-band i{display:block;width:1.5px;height:22px;background:var(--gold);margin:0 12px}
</style>
</head>
<body>
<div class="canvas">
  <main class="flyer">
    <div class="hero-photo" role="img" aria-label="Photo of a smiling family of three cheering in front of their new house with a green lawn and garden"></div>
    <svg class="hero-arch" viewBox="0 0 787 463" aria-hidden="true">
      <defs>
        <linearGradient id="goldArc" x1="0" y1="0" x2="1" y2="0">
          <stop offset="0" stop-color="#c98a3a"/><stop offset=".5" stop-color="#fff2d6"/><stop offset="1" stop-color="#d9a24a"/>
        </linearGradient>
        <linearGradient id="blueArc" x1="0" y1="0" x2="1" y2="0">
          <stop offset="0" stop-color="#1f3f8f"/><stop offset=".5" stop-color="#5b8ac9"/><stop offset="1" stop-color="#1f3f8f"/>
        </linearGradient>
      </defs>
      <circle cx="394" cy="494" r="290" fill="url(#blueArc)"/>
      <circle cx="394" cy="494" r="282" fill="#fff"/>
      <circle cx="394" cy="494" r="260" fill="url(#goldArc)"/>
      <circle cx="394" cy="494" r="250" fill="#fff"/>
      <rect x="0" y="463" width="787" height="60" fill="#fff"/>
    </svg>
    <p class="headline headline-lead">YOU CHOOSE</p>
    <h1 class="headline headline-main">BLUEWATER</h1>
    <p class="headline headline-tag"><i></i><span>we'll carry it home</span><i></i></p>

    <div class="section-title"><i></i><h2>We specialize in</h2><i></i></div>

    <section class="product-card card-fha">
      <div class="card-icon"><svg width="44" height="52" viewBox="0 0 44 52" fill="none" stroke="#fff" stroke-width="2"><rect x="12" y="2" width="28" height="46" rx="2"/><rect x="8" y="5" width="28" height="44" rx="2"/><path d="M13 16h18M13 20h14M13 24h16M13 28h12"/><text x="12" y="13" fill="#fff" stroke="none" font-family="Outfit,sans-serif" font-size="8" font-weight="600">LOAN</text><circle cx="8" cy="44" r="7" fill="none"/><path d="M4.5 44l2.5 2.5 4.5-5"/></svg></div>
      <h3>FHA Loans</h3>
      <ul>
        <li><svg width="14" height="14" viewBox="0 0 14 14"><circle cx="7" cy="7" r="7" fill="var(--deep-blue)"/><path d="M4 7.2l2 2 4-4" stroke="#fff" stroke-width="1.6" fill="none"/></svg>Credit Scores as low as 500</li>
        <li><svg width="14" height="14" viewBox="0 0 14 14"><circle cx="7" cy="7" r="7" fill="var(--deep-blue)"/><path d="M4 7.2l2 2 4-4" stroke="#fff" stroke-width="1.6" fill="none"/></svg>203K Renovation Loans</li>
      </ul>
    </section>

    <section class="product-card card-conv">
      <div class="card-icon"><svg width="44" height="52" viewBox="0 0 44 52" fill="none" stroke="#fff" stroke-width="2"><rect x="12" y="2" width="28" height="46" rx="2"/><rect x="8" y="5" width="28" height="44" rx="2"/><path d="M13 16h18M13 20h14M13 24h16M13 28h12"/><text x="12" y="13" fill="#fff" stroke="none" font-family="Outfit,sans-serif" font-size="8" font-weight="600">LOAN</text><circle cx="8" cy="44" r="7" fill="none"/><path d="M4.5 44l2.5 2.5 4.5-5"/></svg></div>
      <h3>Conventional Loans</h3>
      <ul>
        <li><svg width="14" height="14" viewBox="0 0 14 14"><circle cx="7" cy="7" r="7" fill="var(--deep-blue)"/><path d="M4 7.2l2 2 4-4" stroke="#fff" stroke-width="1.6" fill="none"/></svg>As little as 1% Down</li>
        <li><svg width="14" height="14" viewBox="0 0 14 14"><circle cx="7" cy="7" r="7" fill="var(--deep-blue)"/><path d="M4 7.2l2 2 4-4" stroke="#fff" stroke-width="1.6" fill="none"/></svg>Bank Statement for Self-Employed</li>
      </ul>
    </section>

    <section class="product-card card-inv">
      <div class="card-icon"><svg width="44" height="52" viewBox="0 0 44 52" fill="none" stroke="#fff" stroke-width="2"><rect x="12" y="2" width="28" height="46" rx="2"/><rect x="8" y="5" width="28" height="44" rx="2"/><path d="M13 16h18M13 20h14M13 24h16M13 28h12"/><text x="12" y="13" fill="#fff" stroke="none" font-family="Outfit,sans-serif" font-size="8" font-weight="600">LOAN</text><circle cx="8" cy="44" r="7" fill="none"/><path d="M4.5 44l2.5 2.5 4.5-5"/></svg></div>
      <h3>Investor Loans</h3>
      <ul>
        <li><svg width="14" height="14" viewBox="0 0 14 14"><circle cx="7" cy="7" r="7" fill="var(--deep-blue)"/><path d="M4 7.2l2 2 4-4" stroke="#fff" stroke-width="1.6" fill="none"/></svg>DSCR, &amp; Fix &amp; Flip</li>
        <li><svg width="14" height="14" viewBox="0 0 14 14"><circle cx="7" cy="7" r="7" fill="var(--deep-blue)"/><path d="M4 7.2l2 2 4-4" stroke="#fff" stroke-width="1.6" fill="none"/></svg>Commercial &amp; New Construction</li>
      </ul>
    </section>

    <p class="other-programs"><strong>Other Programs</strong><i></i>HELOCS &amp; Reverse Mortgages</p>

    <div class="cta-band">
      <span class="cta-text">Call today for a free consultation</span>
      <span class="cta-phone"><svg width="20" height="20" viewBox="0 0 20 20" fill="none" stroke="var(--deep-blue)" stroke-width="1.5"><circle cx="10" cy="10" r="9"/><path d="M7 5.5l1.5 2.5-1 1.2c.7 1.4 1.8 2.5 3.2 3.2l1.2-1 2.5 1.5-.8 1.8c-3.8-.2-7.2-3.6-7.4-7.4z"/></svg>(800) 641-2957</span>
    </div>
    <div class="contact-band">www.bluewaterlendhub.com<i></i>NMLS #731846</div>

    <div class="brand-seal"><span class="brand-dot"></span><span class="brand-name">Bluewater</span></div>
  </main>
</div>
</body>
</html>
```